HMC Business Card Design

We need a business card design for a new company called ' Harbour Mill Coffee'. We are a mobile Coffee Trailer providing Espresso Coffee, Specialty Tea's, Milkshakes, Iced Coffee & Iced Chocolate, Soft drinks and Gourmet Cookies to Sporting Events, Fetes, Animal Shows etc...
We would like Darren's name and mobile phone number on the card along with the harbour mill email address and a link to our facebook page Harbour Mill Coffee.
Can you please attach the Harbour Mill Logo to the business card.
I have tried to attach our logo and a picture of our mobile trailer to give you an idea of how we would like the design similar to the trailer if possible. If these pictures and logo's are not attached please email me and i will send them through.

Contact Information for Business Card

Darren Wilkes
0491 372 806
harbourmillcoffee@mailbox-demo.net
FB Harbour Mill Coffee

Requirements
Must have
• We would like coffee beans in the back ground of the card.

```html
<!DOCTYPE html>
<html lang="en">
<head>
<meta charset="utf-8">
<title>Harbour Mill Coffee – Business Card</title>
<link rel="stylesheet" href="https://fonts.googleapis.com/css2?family=Open+Sans:wght@400;700&family=Courgette&display=swap">
<style>
  :root {
    --page: #ffffff;
    --ink: #1e1a17;
    --roast: #6b3a22;
    --roast-deep: #4a2614;
    --crema: #c9a27e;
    --bean-light: #e3cbb3;
    --bean-mid: #a8754d;
    --bean-dark: #6e3f23;
    --pattern: #eadbcc;
    --mark: #2a1d16;
  }
  * { margin: 0; padding: 0; box-sizing: border-box; }
  html, body { width: 1200px; height: 353px; overflow: hidden; background: var(--page); }
  body { position: relative; font-family: "Open Sans", Arial, sans-serif; color: var(--ink); }

  .card { position: absolute; overflow: hidden; }
  .card--front { left: 15px; top: 25px; width: 520px; height: 303px; }
  .card--back  { left: 662px; top: 25px; width: 520px; height: 297px; background: var(--page); }

  .bean-photo {
    position: absolute; inset: 0;
    background:
      linear-gradient(90deg, rgba(255,255,255,0.95) 0%, rgba(255,255,255,0.75) 22%, rgba(255,255,255,0.3) 48%, rgba(255,255,255,0.2) 100%),
      radial-gradient(ellipse at 70% 30%, var(--bean-light) 0%, var(--bean-mid) 60%, var(--bean-dark) 100%);
  }
  .bean-pattern {
    position: absolute; left: 0; top: 0; width: 100%; height: 260px;
    background:
      linear-gradient(180deg, rgba(255,255,255,0.35) 0%, rgba(255,255,255,0.1) 100%),
      var(--pattern);
  }
  .wave { position: absolute; left: 0; bottom: 0; width: 100%; height: 120px; }

  .brand {
    position: absolute; left: 16px; top: 136px;
    display: flex; align-items: center; gap: 8px;
    font-size: 17px; font-weight: 400; color: var(--mark);
  }
  .brand__dot { width: 14px; height: 14px; border-radius: 50%; background: var(--mark); }

  .social {
    position: absolute; left: 16px; top: 163px;
    font-size: 13.5px; color: var(--ink);
  }

  .person { position: absolute; left: 265px; top: 22px; }
  .person__name { font-size: 20px; font-weight: 700; color: var(--ink); line-height: 1.2; }
  .person__role { font-family: "Courgette", cursive; font-size: 17px; color: var(--roast); margin-top: 2px; }

  .contacts {
    position: absolute; left: 250px; top: 139px;
    font-size: 13.5px; line-height: 20px; color: var(--ink); list-style: none;
  }

  .services {
    position: absolute; left: 0; top: 11px; width: 100%;
    text-align: center; font-size: 15.5px; line-height: 23px; color: var(--ink);
  }
</style>
</head>
<body>

  <section class="card card--front" aria-label="Card front">
    <div class="bean-photo" role="img" aria-label="Background photograph of roasted coffee beans"></div>
    <svg class="wave" viewBox="0 0 520 120" preserveAspectRatio="none" aria-hidden="true">
      <defs>
        <linearGradient id="front-lower" x1="0" y1="0" x2="0" y2="1">
          <stop offset="0" stop-color="#7a4a2c" stop-opacity="0.8"/>
          <stop offset="1" stop-color="#4a2614" stop-opacity="0.9"/>
        </linearGradient>
        <linearGradient id="front-band" x1="0" y1="0" x2="1" y2="0">
          <stop offset="0" stop-color="#c9a27e"/>
          <stop offset="0.5" stop-color="#8e5a38"/>
          <stop offset="1" stop-color="#b5865f"/>
        </linearGradient>
      </defs>
      <path d="M0 18 C80 40 150 40 230 22 C300 6 380 4 520 12 L520 120 L0 120 Z" fill="url(#front-lower)"/>
      <path d="M0 12 C80 34 150 34 230 16 C300 0 380 -2 520 6 L520 16 C380 8 300 12 230 28 C150 46 80 46 0 24 Z" fill="url(#front-band)"/>
    </svg>

    <div class="brand"><span class="brand__dot"></span><span class="brand__name">Harbour Mill Coffee</span></div>
    <p class="social">FB Harbour Mill Coffee</p>

    <div class="person">
      <p class="person__name">Name Name</p>
      <p class="person__role">Managing Director</p>
    </div>

    <ul class="contacts">
      <li>Darren Wilkes 0491 372 806</li>
      <li>Nadia Forbes 0472 158 930</li>
      <li>harbourmillcoffee@mailbox-demo.net</li>
    </ul>
  </section>

  <section class="card card--back" aria-label="Card back">
    <div class="bean-pattern" role="img" aria-label="Faint repeating pattern of coffee beans"></div>
    <svg class="wave" viewBox="0 0 520 120" preserveAspectRatio="none" aria-hidden="true">
      <defs>
        <linearGradient id="back-lower" x1="0" y1="0" x2="1" y2="0">
          <stop offset="0" stop-color="#e8d6c4"/>
          <stop offset="0.45" stop-color="#c9a27e"/>
          <stop offset="1" stop-color="#6b3a22"/>
        </linearGradient>
        <linearGradient id="back-band" x1="0" y1="0" x2="1" y2="0">
          <stop offset="0" stop-color="#d9bfa5"/>
          <stop offset="0.5" stop-color="#8e5a38"/>
          <stop offset="1" stop-color="#5a3019"/>
        </linearGradient>
      </defs>
      <path d="M0 30 C90 30 170 -2 260 6 C340 14 420 38 520 26 L520 120 L0 120 Z" fill="url(#back-lower)"/>
      <path d="M0 22 C90 22 170 -10 260 -2 C340 6 420 30 520 18 L520 28 C420 40 340 16 260 8 C170 0 90 32 0 32 Z" fill="url(#back-band)"/>
    </svg>

    <p class="services">
      We are<br>
      a mobile Coffee Trailer<br>
      providing Espresso Coffee,<br>
      Specialty Tea’s, Milkshakes,<br>
      Iced Coffee &amp; Iced Chocolate,<br>
      Soft drinks and Gourmet Cookies<br>
      to Sporting Events, Fetes, Animal Shows etc…
    </p>
  </section>

</body>
</html>
```